Harborline 4 Trades Pwrpt Design

I need a professional PWRPT template around Harborline4trades. The website associated http://harborline4trades.example/ . I have included several documents that highlight our color pallet and goals. The template will serve as a tool to tell our story as a company.
BACKGROUND: We also own QM7lr (Bridgewell Advisory 7 Learning www.qm7lr.example ). QM7lr offers research-policy-and practical solutions for educators. Our Harborline 4 Trades was born out of one of these solutions. QM7lr (We) just launched the H4T solution.
Associated websites for reference:
http://harborline4trades.example/
http://www.qm7lr.example/

```html
<!DOCTYPE html>
<html lang="en">
<head>
<meta charset="utf-8">
<title>Harborline 4 Trades – Slide Template</title>
<link rel="stylesheet" href="https://fonts.googleapis.com/css2?family=Carlito:wght@400;700&display=swap">
<style>
  :root {
    --brand-orange: #f7941d;
    --band-grey: #555555;
    --slide-white: #ffffff;
    --title-ink: #111111;
  }
  html, body {
    margin: 0;
    padding: 0;
    overflow: hidden;
    background: var(--slide-white);
  }
  .slide {
    position: relative;
    width: 1200px;
    height: 900px;
    overflow: hidden;
    background: var(--slide-white);
    font-family: "Carlito", "Calibri", sans-serif;
  }
  .header-wave {
    position: absolute;
    top: 0;
    left: 0;
    width: 1200px;
    height: 240px;
  }
  .header-wave .wave-fill { fill: var(--brand-orange); }
  .header-wave .wave-rule { fill: var(--band-grey); }
  .slide-title {
    position: absolute;
    top: 8px;
    left: 15px;
    margin: 0;
    font-size: 36px;
    font-weight: 400;
    color: var(--title-ink);
    line-height: 1.2;
  }
  .brand-mark {
    position: absolute;
    top: 26px;
    right: 22px;
    width: 166px;
    height: 116px;
    margin: 0;
    display: flex;
    align-items: center;
    justify-content: center;
    gap: 10px;
  }
  .brand-dot {
    width: 18px;
    height: 18px;
    border-radius: 50%;
    background: var(--slide-white);
    flex: none;
  }
  .brand-name {
    font-size: 80px;
    font-weight: 700;
    color: var(--slide-white);
    line-height: 1;
    letter-spacing: 1px;
  }
  .footer-bar {
    position: absolute;
    left: 0;
    bottom: 0;
    width: 1200px;
    height: 38px;
    background: var(--band-grey);
    color: var(--slide-white);
    display: flex;
    align-items: center;
    justify-content: space-between;
    padding: 0 12px;
    box-sizing: border-box;
    font-size: 16px;
    font-weight: 700;
  }
</style>
</head>
<body>
  <main class="slide">
    <svg class="header-wave" viewBox="0 0 1200 240" aria-hidden="true">
      <path class="wave-fill" d="M0,0 H1200 V210 C950,128 600,66 0,64 Z"/>
      <path class="wave-rule" d="M0,68 C600,70 950,132 1200,214 L1200,228 C950,144 600,80 0,78 Z"/>
    </svg>
    <h1 class="slide-title">Project Title Here</h1>
    <div class="brand-mark">
      <span class="brand-dot"></span>
      <span class="brand-name">H4T</span>
    </div>
    <footer class="footer-bar">
      <span class="footer-copyright">Copyright text here</span>
      <span class="footer-page">Page : 01</span>
    </footer>
  </main>
</body>
</html>
```